Keepers of the Salt Roads book cover

My goal is to choose a submission ready cover for my self-published book. I am looking for an illustrative design that coordinates with the mood of the book, and with current market expectations.

Attached for context are three prior drafts of the cover. My desire is for something more illustrative (like the first one) than obvious AI, like the other two. The story takes place in a fictional town in the Arizona desert. The landscape is a big part of the story. So I would like the mood and color palette to reflect the desert. Reflect; not be a photorealistic depiction of desert. It need not portray the desert explicitly at all, if the design can invoke it. The book does have a fantasy story, but I do not want a "fantasy book" cover. Something more contemporary in design and font choices.

For example, this cover invokes the sea: https://www.bookvarnel.example/item/47213

This one invokes a forest at night: https://www.bookvarnel.example/item/58324

And this one a different take on the sea: https://www.bookvarnel.example/item/69435

(By the way, my book with its current cover, which I hate, is at:)
https://www.bookvarnel.example/item/70546

Target Market(s)

25-80 year old, professional females.

Font styles to use
Other font styles liked:
• For the Author Name, use upper and lower case (i.e., Dale Worthen), with Abadi font, if possible. In the title, make "of the" lower case.

Requirements
Must have
• Copper Wren logo on the spine, with the words "Copper Wren" beneath it.

```html
<!DOCTYPE html>
<html lang="en">
<head>
<meta charset="utf-8">
<title>Keepers of the Salt Roads — Full Cover</title>
<link rel="stylesheet" href="https://fonts.googleapis.com/css2?family=Oswald:wght@500;600;700&family=Montserrat:wght@400;500&family=Mulish:wght@600;700&display=swap">
<style>
  :root {
    --stage: #a9a9ab;
    --back-clay: #6b3a2a;
    --spine-umber: #2a1812;
    --sky-glow: #f3cf9a;
    --sky-mid: #d98a56;
    --sky-deep: #8f4a3a;
    --mesa-rose: #7a3c34;
    --ground-umber: #2c1914;
    --ink-light: #fff8ef;
  }
  * { margin: 0; padding: 0; box-sizing: border-box; }
  html, body { width: 1200px; height: 1200px; overflow: hidden; background: var(--stage); }
  .spread { position: absolute; left: 29px; top: 188px; width: 1141px; height: 824px; }

  .back-cover {
    position: absolute; left: 0; top: 0; width: 551px; height: 824px;
    background: var(--back-clay); color: var(--ink-light);
    font-family: "Montserrat", sans-serif; font-weight: 500; font-size: 15.3px; line-height: 18px;
  }
  .blurb { position: absolute; left: 28px; top: 37px; width: 500px; }
  .blurb p { margin-bottom: 17px; }
  .author-bio { position: absolute; left: 31px; top: 540px; width: 520px; display: flex; gap: 13px; }
  .author-photo { flex: 0 0 79px; height: 116px; background: linear-gradient(160deg, #a89a90, #5f5149); border: 1px solid #d9cbbf; }
  .author-bio p { width: 405px; }

  .spine {
    position: absolute; left: 551px; top: 0; width: 40px; height: 824px;
    background: var(--spine-umber); color: var(--ink-light);
  }
  .spine-title, .spine-author {
    position: absolute; left: 20px; writing-mode: vertical-rl; white-space: nowrap;
    transform: translateX(-50%);
  }
  .spine-title { top: 44px; font-family: "Oswald", sans-serif; font-weight: 700; font-size: 19px; letter-spacing: 0.3px; }
  .spine-title .lower { font-weight: 600; }
  .spine-author { top: 604px; font-family: "Mulish", sans-serif; font-weight: 700; font-size: 20px; letter-spacing: 1px; }
  .publisher-mark { position: absolute; left: 0; top: 448px; width: 40px; text-align: center; }
  .publisher-mark .dot { display: block; width: 22px; height: 22px; margin: 0 auto 4px; border-radius: 50%; background: var(--ink-light); }
  .publisher-mark .name { font-family: "Montserrat", sans-serif; font-weight: 500; font-size: 5.5px; white-space: nowrap; }

  .front-cover { position: absolute; left: 591px; top: 0; width: 550px; height: 824px; }
  .front-cover svg { display: block; }
</style>
</head>
<body>
<main class="spread">
  <section class="back-cover">
    <div class="blurb">
      <p>Lucas Grant, a sharp-minded but skeptical scientist, arrives in Redstone, Arizona, with one goal: to debunk the age-old myths surrounding the salt roads. But what begins as a methodical investigation into unexplained energy readings quickly spirals into a journey fraught with mystery, danger, and an unsettling clash between science and the unexplainable.</p>
      <p>As Lucas uncovers bizarre data he can’t rationalize, his path crosses with Sierra Castillo, a fiercely independent artist who draws her strength from the desert’s ancient rhythms. Deeply connected to the land and its hidden energies, Sierra’s insights defy Lucas’s logic and force him to confront truths far older—and more powerful—than anything in his textbooks.</p>
      <p>Together, they delve into the salt roads’ enigmatic power, uncovering a story woven with mystic lore, ecological activism, and a battle for the heart of a community threatened by corporate greed. As the pulse of the Earth calls to Lucas, he must decide: will he cling to the safety of skepticism, or embrace the wonder and responsibility of a force that could rewrite everything he thought he knew?</p>
      <p>With breathtaking desert landscapes, unforgettable characters, and a seamless blend of science and magic, Keepers of the Salt Roads invites readers on an exhilarating quest for truth. Can Lucas and Sierra save Redstone’s future—or will the salt roads’ secrets remain buried forever?</p>
    </div>
    <div class="author-bio">
      <div class="author-photo" role="img" aria-label="Author portrait photograph"></div>
      <p>Dale Worthen, a native of Utah, weaves themes of mysticism, cultural heritage, and the wonders of the American West into his novels. Influenced by a love of storytelling, faith, and the great outdoors, Dale’s work explores profound human connections through captivating characters and richly detailed settings.</p>
    </div>
  </section>

  <section class="spine">
    <div class="spine-title">KEEPERS <span class="lower">of the</span> SALT ROADS</div>
    <div class="publisher-mark"><span class="dot"></span><span class="name">Copper Wren</span></div>
    <div class="spine-author">Dale Worthen</div>
  </section>

  <section class="front-cover">
    <svg width="550" height="824" viewBox="0 0 550 824" xmlns="http://www.w3.org/2000/svg">
      <defs>
        <radialGradient id="sky-glow" cx="0.72" cy="0.22" r="0.85">
          <stop offset="0" stop-color="#f3cf9a"/>
          <stop offset="0.4" stop-color="#d98a56"/>
          <stop offset="1" stop-color="#8f4a3a"/>
        </radialGradient>
        <linearGradient id="scene-tone" x1="0" y1="0" x2="0" y2="1">
          <stop offset="0" stop-color="#9a4d3a" stop-opacity="0"/>
          <stop offset="0.35" stop-color="#8a4636"/>
          <stop offset="0.75" stop-color="#5a2e25"/>
          <stop offset="1" stop-color="#2c1914"/>
        </linearGradient>
      </defs>
      <rect class="sky" width="550" height="824" fill="url(#sky-glow)"/>
      <rect class="desert-scene" x="0" y="380" width="550" height="444" fill="url(#scene-tone)" role="img" aria-label="Illustration of mesa and saguaro silhouettes across a dusky salt flat"/>
      <rect class="ground-band" x="0" y="684" width="550" height="140" fill="#2c1914"/>
      <g class="cover-title" fill="#fff8ef" font-family="Oswald, sans-serif" font-weight="700">
        <text x="81" y="118" font-size="98" textLength="438" lengthAdjust="spacingAndGlyphs">KEEPERS</text>
        <text x="166" y="186" font-size="70" font-weight="500" textLength="214" lengthAdjust="spacingAndGlyphs">of the</text>
        <text x="121" y="404" font-size="236" textLength="372" lengthAdjust="spacingAndGlyphs">SALT</text>
        <text x="121" y="544" font-size="148" textLength="358" lengthAdjust="spacingAndGlyphs">ROADS</text>
      </g>
      <text class="cover-author" x="268" y="782" text-anchor="middle" fill="#fff8ef" font-family="Mulish, sans-serif" font-weight="700" font-size="44" letter-spacing="3">Dale Worthen</text>
    </svg>
  </section>
</main>
</body>
</html>
```